Breezeway Climate Business Card Design

Design new, 2 sides, business cards for a residential and light commercial heating, air conditioning contractor.

Target Market(s)

Homeowners, small businesses

Industry/Entity Type

Business

Contact Information for Business Card

Dominic Vasquerelli
Phone - 555-214-6837
Email
Address - PO box 618
Millbrook NJ 07999
Website - www.BreezewayClimateLLC.example

Requirements
Must have
• logo, company colors, standard size with no die cut, so I can use printhaven

```html
<!DOCTYPE html>
<html lang="en">
<head>
<meta charset="utf-8">
<title>Breezeway Climate – Business Card</title>
<link rel="stylesheet" href="https://fonts.googleapis.com/css2?family=Roboto+Condensed:wght@400;700&display=swap">
<style>
  :root {
    --backdrop: #3d3442;
    --card-white: #ffffff;
    --crimson: #b8113f;
    --orange: #ff7a10;
    --black: #111111;
    --signal-red: #ff1a1a;
    --ink: #1a1a1a;
    --icon-red: #c8102e;
  }
  html, body {
    margin: 0;
    width: 1200px;
    height: 800px;
    overflow: hidden;
    background: var(--backdrop);
    font-family: "Roboto Condensed", Arial, sans-serif;
  }
  .stage {
    width: 1200px;
    height: 800px;
    display: flex;
    align-items: center;
    justify-content: center;
    gap: 60px;
  }
  .card {
    width: 520px;
    height: 297px;
    display: block;
    box-shadow: 0 10px 30px rgba(0,0,0,.45);
    background: var(--card-white);
  }
  .fill-white { fill: var(--card-white); }
  .fill-crimson { fill: var(--crimson); }
  .fill-orange { fill: var(--orange); }
  .fill-black { fill: var(--black); }
  .fill-red { fill: var(--signal-red); }
  .brand-name {
    fill: var(--crimson);
    font-family: "Roboto Condensed", Arial, sans-serif;
    font-weight: 700;
    font-size: 34px;
    text-transform: uppercase;
  }
  .holder-name {
    fill: var(--card-white);
    font-weight: 700;
    font-size: 17px;
    text-transform: uppercase;
  }
  .tagline {
    fill: var(--card-white);
    font-size: 14px;
    text-transform: uppercase;
  }
  .contact-line {
    fill: var(--ink);
    font-size: 12.5px;
  }
  .contact-icon {
    fill: none;
    stroke: var(--icon-red);
    stroke-width: 1.4;
    stroke-linecap: round;
    stroke-linejoin: round;
  }
</style>
</head>
<body>
<main class="stage">

  <!-- Front side -->
  <svg class="card card-front" viewBox="0 0 520 297" aria-label="Business card front">
    <rect class="fill-white" width="520" height="297"/>
    <polygon class="fill-orange" points="0,108 30,108 46,124 474,124 490,108 520,108 520,176 490,176 474,160 46,160 30,176 0,176"/>
    <rect class="fill-white" x="66" y="112" width="388" height="62"/>
    <rect class="fill-crimson" x="84" y="132" width="20" height="20"/>
    <text class="brand-name" x="118" y="155" textLength="318" lengthAdjust="spacingAndGlyphs">Breezeway Climate</text>
  </svg>

  <!-- Back side -->
  <svg class="card card-back" viewBox="0 0 520 297" aria-label="Business card back">
    <rect class="fill-white" width="520" height="297"/>
    <path class="fill-crimson" d="M0 0 H285 C250 50 235 110 232 150 H0 Z"/>
    <rect class="fill-orange" x="0" y="150" width="520" height="52"/>
    <rect class="fill-black" x="0" y="202" width="520" height="16"/>
    <rect class="fill-red" x="380" y="202" width="60" height="16"/>
    <rect class="fill-crimson" x="0" y="218" width="520" height="79"/>

    <circle class="fill-orange" cx="120" cy="38" r="14"/>
    <text class="holder-name" x="120" y="84" text-anchor="middle">Dominic Vasquerelli</text>

    <text class="tagline" x="20" y="172">Residential and light commercial heating</text>
    <text class="tagline" x="20" y="190">air conditioning contractor</text>

    <g class="contact-list">
      <text class="contact-line" x="474" y="32" text-anchor="end">555-214-6837</text>
      <text class="contact-line" x="474" y="62" text-anchor="end">www.BreezewayClimateLLC.example</text>
      <text class="contact-line" x="474" y="92" text-anchor="end">PO box 618, Millbrook NJ 07999</text>
      <text class="contact-line" x="474" y="122" text-anchor="end">yourid@BreezewayClimateLLC.example</text>
    </g>

    <g class="contact-icon">
      <path d="M489 21 c2 -1 4 0 4 0 l2 4 -2 2 c1 3 3 5 6 6 l2 -2 4 2 c0 0 1 2 0 4 c-8 1 -17 -8 -16 -16 Z"/>
      <circle cx="497" cy="58" r="8"/>
      <ellipse cx="497" cy="58" rx="3.5" ry="8"/>
      <line x1="489" y1="58" x2="505" y2="58"/>
      <path d="M497 97 c-5 -6 -7 -8 -7 -11 a7 7 0 0 1 14 0 c0 3 -2 5 -7 11 Z"/>
      <circle cx="497" cy="86" r="2.5"/>
      <rect x="489" y="112" width="16" height="12"/>
      <path d="M489 112 l8 7 8 -7"/>
    </g>
  </svg>

</main>
</body>
</html>
```